Webpage for co-working space for tech startups

We have an established co-working space in Aalborg Denmark where we have around 30 companies sharing office space. We are starting a new chapter for us and would like to have a new graphical image - new logo and new webpage, but keep the same name. The webpage should be professional, but also "fun", not too serious. We are all about working hard on our companies, but also taking some time off in between and being social and having fun. We are not corporate, but want to project the image that we are serious about what we do.

We currently have a black/red logo (see www.pebblehive.dk or test.pebblehive.dk), but are interesting in having a new logo design, so colour can be chosen freely. Currently our logo is a big PEBBLE and a little hive underneath the PEBBLE. The new logo will be one word "pebblehive" with a small logo before or on top.

If we can make a good webpage for this project, then I have a second more simple project which is also a small single page wordpress site which I would also like to have made.

Target Market(s)

tech startups - relatively new companies, typically younger people 20-35 with a tech background - business or programming, preferably both

Industry/Entity Type

PEBBLE

Logo Text

pebblehive

Coding

Coded - Design and coding required

Number of Pages Required

4 page

Font styles to use
Sans Serif

Colors

Designer to choose colors to be used in the design.

Requirements
Must have
• Wordpress CMS.
• Mobile and PC optimized
• 2 languages - English and Danish
• Four sections, could be four pages, or four sections of a single page.
• "Home", "Residents", "Our Working Space", "Our Event Space"
• Footer of page or pages should have contact information.
• "Home" has some information about who we are and what we do
• "Residents" has a list of all our residents - it should be possible to easily add and removed new / old residents - See one example here: http://test.pebblehive.dk/en_GB/beboere/ or another example here: http://www.pebblehive.dk/beboere/ - one of our colleagues http://quillbarn.dk/startups/ or another one of our colleagues http://www.copperdeckhall.dk/residents/
• "Our working space" will have a description of our building, a map of where it is and a bunch of photos which show the different offices, meeting rooms and people working
• "Our events space" will have a description of our event spaces, details of cost + different arrangments of furniture, and lots of photos of events, see here for an example http://www.pebblehive.dk/lej-vores-lokaler/
• Our current webpage - www.pebblehive.dk was put together very quickly and has not really been optimized. We started a new webpage test.pebblehive.dk, but it was never really finished.
• We are looking for a simple webpage, not too much going on. Examples of some of our colleagues in the business http://quillbarn.dk/, http://www.copperdeckhall.dk/,
Nice to have
• http://www.copperdeckhall.dk/ is a really good template for us. If we can get something like this, we are happy.

```html
<!DOCTYPE html>
<html lang="en">
<head>
<meta charset="utf-8">
<title>Pebblehive – Co-working for tech startups</title>
<link href="https://fonts.googleapis.com/css2?family=Montserrat:wght@400;600;700&family=Open+Sans:wght@400;600&display=swap" rel="stylesheet">
<style>
:root{
  --accent:#e8543f;
  --ink:#222222;
  --dark:#2c2c2c;
  --darker:#1f1f1f;
  --black:#0d0d0d;
  --white:#ffffff;
  --muted:#9a9a9a;
  --heading:"Montserrat",Arial,sans-serif;
  --body:"Open Sans",Arial,sans-serif;
}
*{box-sizing:border-box;margin:0;padding:0}
html,body{width:1200px;height:3984px;overflow:hidden}
body{font-family:var(--body);color:var(--ink);background:var(--black)}

.site-header{height:80px;background:var(--white);display:flex;align-items:center;justify-content:space-between;padding:0 28px}
.brand{font-family:var(--heading);font-weight:700;font-size:22px;color:var(--ink);display:flex;align-items:center;gap:8px;line-height:1}
.brand-dot{width:16px;height:16px;border-radius:50%;background:var(--accent)}
.main-nav{display:flex;gap:26px;font-size:14px;color:#555}

.hero{height:580px;position:relative;display:flex;align-items:center;justify-content:center;text-align:center}
.hero-photo{position:absolute;inset:0;background:linear-gradient(180deg,#8e969c 0%,#5c6166 45%,#3a3a3a 75%,#2a2522 100%)}
.hero-title{position:relative;font-family:var(--heading);font-weight:700;font-size:50px;line-height:1.2;color:var(--white);letter-spacing:1px;margin-top:-30px}

.residents{height:720px;background:var(--white);padding-top:48px}
.section-title{font-family:var(--heading);font-weight:700;font-size:40px;text-align:center;letter-spacing:1px}
.resident-grid{display:grid;grid-template-columns:repeat(4,320px);justify-content:center;row-gap:58px;margin-top:76px}
.resident{display:flex;flex-direction:column;align-items:center}
.resident-badge{width:152px;height:152px;border-radius:50%;border:6px solid #f0f0f0;box-shadow:0 2px 6px rgba(0,0,0,.12);display:flex;align-items:center;justify-content:center;font-family:var(--heading);font-weight:600;font-size:17px;color:#6b8a3a;background:var(--white)}
.resident-badge.is-dark{background:#1d2226;color:var(--white)}
.resident-name{margin-top:16px;font-size:14px;font-weight:600;color:#444;letter-spacing:.5px}

.spacer{height:60px;background:var(--black)}

.about{height:400px;background:var(--dark);padding:56px 60px 0;color:var(--white);margin:0 16px}
.about .section-title{font-size:36px}
.about-text{margin-top:48px;font-size:15px;line-height:1.9;color:#b9b9b9;text-align:center}

.sponsors-wrap{height:432px;background:var(--black);padding:28px 32px 0}
.sponsors{height:404px;background:var(--white);padding-top:48px}
.sponsor-row{display:flex;justify-content:space-around;align-items:center;margin-top:110px;padding:0 30px}
.sponsor{font-family:var(--heading);font-weight:600;font-size:26px;color:#1e3f6e}

.contact{height:568px;position:relative;color:var(--white)}
.contact-photo{position:absolute;inset:0;background:linear-gradient(180deg,#474747 0%,#3b3532 50%,#2b2726 100%)}
.contact-inner{position:relative;padding:48px 68px 0}
.contact .section-title{font-size:36px}
.contact-form{margin-top:70px;display:grid;grid-template-columns:1fr 1fr 1fr;gap:30px}
.field{height:40px;background:var(--white);font-size:13px;color:var(--muted);padding:11px 12px}
.field.message{grid-column:1/4;height:240px;margin-top:-10px}
.send{grid-column:3;justify-self:end;background:var(--accent);color:var(--white);font-size:13px;font-weight:600;padding:13px 22px;margin-top:-14px}

.location{height:932px;background:var(--dark);padding:52px 68px 0;color:var(--white)}
.location-title{font-family:var(--heading);font-weight:700;font-size:50px;line-height:1.2;letter-spacing:.5px}
.location-rule{width:370px;height:4px;background:var(--accent);margin-top:42px}
.map{margin-top:56px;height:632px;background:linear-gradient(135deg,#e9e6df 0%,#d8d4cb 50%,#a9cbe6 100%)}

.site-footer{height:212px;background:var(--darker);display:flex;color:#bdbdbd;font-size:13px}
.footer-contacts{flex:1;display:grid;grid-template-columns:repeat(3,1fr);align-items:center;text-align:center;padding:0 20px}
.footer-item{display:flex;flex-direction:column;align-items:center;gap:12px}
.footer-social{width:290px;background:#141414;display:flex;flex-direction:column;align-items:center;justify-content:center;gap:14px}
.social-dots{display:flex;gap:10px}
.social-dots span{width:12px;height:12px;border-radius:50%;background:#bdbdbd}
.copyright{font-size:12px;color:var(--muted)}
</style>
</head>
<body>

<header class="site-header">
  <div class="brand"><span class="brand-dot"></span>PEBBLE</div>
  <nav class="main-nav"><span>Home</span><span>Our Event Space</span><span>Our Working Space</span><span>Residents</span></nav>
</header>

<section class="hero">
  <div class="hero-photo" role="img" aria-label="Photo of a city street with tall buildings at dusk"></div>
  <h1 class="hero-title">PEBBLE HIVE , WE ARE A TECH<br>COMPANY... TRY US OUT</h1>
</section>

<section class="residents">
  <h2 class="section-title">RESIDENTS</h2>
  <div class="resident-grid">
    <div class="resident"><div class="resident-badge">orvela</div><span class="resident-name">ORVELA</span></div>
    <div class="resident"><div class="resident-badge">tallpine</div><span class="resident-name">TALLPINE</span></div>
    <div class="resident"><div class="resident-badge">hexagate</div><span class="resident-name">HEXAGATE</span></div>
    <div class="resident"><div class="resident-badge is-dark">crewshift</div><span class="resident-name">CREWSHIFT</span></div>
    <div class="resident"><div class="resident-badge">makefield</div><span class="resident-name">MAKEFIELD</span></div>
    <div class="resident"><div class="resident-badge">ledgerly</div><span class="resident-name">LEDGERLY</span></div>
    <div class="resident"><div class="resident-badge">boxbright</div><span class="resident-name">BOXBRIGHT</span></div>
    <div class="resident"><div class="resident-badge">QM</div><span class="resident-name">QM</span></div>
  </div>
</section>

<div class="spacer"></div>

<section class="about">
  <h2 class="section-title">PEBBLE HIVE</h2>
  <p class="about-text">We are a co-working space in the heart of Aalborg where around thirty tech startups share offices, ideas and coffee. Our residents build software, hardware and new business models, and they help each other along the way. We work hard on our companies, but we also make time for Friday bars, talks, hackathons and long lunches on the terrace. If you are starting something new and want good neighbours, flexible desks and a friendly community, come and visit us and see if you fit in.</p>
</section>

<div class="sponsors-wrap">
  <section class="sponsors">
    <h2 class="section-title">MAIN SPONSORS</h2>
    <div class="sponsor-row">
      <span class="sponsor">Halvorsen Law</span>
      <span class="sponsor">Nordmark Bank</span>
      <span class="sponsor">Sentinel</span>
      <span class="sponsor">Velkrone</span>
    </div>
  </section>
</div>

<section class="contact">
  <div class="contact-photo" role="img" aria-label="Photo of a street scene behind the contact form"></div>
  <div class="contact-inner">
    <h2 class="section-title">GET IN TOUCH</h2>
    <form class="contact-form">
      <div class="field">Your Name</div>
      <div class="field">Your Email</div>
      <div class="field">Subject</div>
      <div class="field message">Your Message</div>
      <div class="send">SEND MESSAGE</div>
    </form>
  </div>
</section>

<section class="location">
  <h2 class="location-title">OUR OFFICE ADDRESS AND LOCATION<br>(CLICK TO VIEW EXPANDED VERSION)</h2>
  <div class="location-rule"></div>
  <div class="map" role="img" aria-label="Map of Aalborg with a pin marking the office location"></div>
</section>

<footer class="site-footer">
  <div class="footer-contacts">
    <div class="footer-item">
      <svg width="18" height="24" viewBox="0 0 18 24"><path d="M9 0C4 0 0 4 0 9c0 6.5 9 15 9 15s9-8.5 9-15c0-5-4-9-9-9z" fill="var(--accent)"/><circle cx="9" cy="9" r="3.5" fill="#1f1f1f"/></svg>
      <span>Fjordvej 14, 9220 Aalborg Ø, Denmark</span>
    </div>
    <div class="footer-item">
      <svg width="24" height="18" viewBox="0 0 24 18"><rect width="24" height="18" rx="2" fill="#3aa876"/><path d="M1 2l11 8 11-8" stroke="#1f1f1f" stroke-width="2" fill="none"/></svg>
      <span>info@pebblehive.dk</span>
    </div>
    <div class="footer-item">
      <svg width="22" height="22" viewBox="0 0 22 22"><rect width="22" height="22" rx="3" fill="#3b8fd4"/><path d="M7 5l2 3-1.5 1.5a8 8 0 0 0 4 4L13 12l3 2-1 3c-5 0-10-5-10-10z" fill="#1f1f1f"/></svg>
      <span>+45 12 34 56 78</span>
    </div>
  </div>
  <div class="footer-social">
    <div class="social-dots"><span></span><span></span><span></span><span></span></div>
    <span class="copyright">© 2016 Pebblehive. All rights reserved.</span>
  </div>
</footer>

</body>
</html>
```